Modern Label Design for Fruity Drink (300ml PET)

Dear Graphic Designers,

JOB BRIEF
We are a beverage manufacturer in South Africa seeking a creative wrap-around label design for our exciting new fruity drink range called Zindelu. Although our beverage doesn't contain real fruit, it's crafted to emulate the taste and appearance of authentic fruit juices, complete with essential benefits like vitamins and minerals that are contained in real fruit. Despite being priced competitively, we want the design to exude a premium feel likened to luxury juices and drinks.

TARGET MARKET
The design must possess a modern appeal that resonates with both children and adults.

DESIGN GUIDELINES
- Modern and Elegant
- Colourful
- Evokes a sense of fruit without direct explicit fruit depictions

MANDATORY ELEMENTS
1. Flavoured Drink: Law states that "Flavoured Drink" needs to be written on the front of the label, potentially integrated with the flavor name, e.g., "Orange Flavoured Drink."
2. No Fruit Images: Avoid using real fruit images, opting instead for textures and shapes that very slightly allude to the essence of fruit flavour. This is also a legal constraint.
3. Toucan Mascot: Consider incorporating a toucan or parrot as a potential mascot.
4. Logo: We have a logo, you may use this and adapt it, or design your own.
5. Claims: We need a claim on the front "High in Vitamin C, B and Zinc"

DESIGN INSPIRATION AND WARNING
Avoid drawing inspiration from our initial design attempt, shared in the files section. This design is deemed unsuitable as it appears too busy, has an 'old school' vibe, and may be perceived as exclusively for children. We aspire for a premium design that caters to adults while still being colourful.

FLAVORS
"Golden Swirl" or alternatively "Orange Flavoured Drink"
"Velvet Pop" or alternatively "Berry Flavoured Drink"
"Island Drift" or alternatively "Tropical Flavoured Drink"
"Crisp Meadow" or alternatively "Apple Flavoured Drink"

We encourage your innovative designs. Thank you for your participation, and we look forward to witnessing your creative brilliance!

Best regards,
The Marketing Team

Target Market(s)

Adults and Children (Premium)

Industry/Entity Type

Beverages

Colors

Designer to choose colors to be used in the design.

Requirements
Must have
• Premium and Colourful
Nice to have
• It would be nice to have a new or updated logo (but we have existing logo if needed), and it would be nice to have a parrot or toucan mascot somewhere
Should not have
• Looking too much like a children's fruity drink. Shouldn't contain real images or illustrations of fruit (only vaguely resembling the fruit through shapes and textures)

```html
<!DOCTYPE html>
<html lang="en">
<head>
<meta charset="utf-8">
<title>Zindelu Flavoured Drink – Wrap-around Labels</title>
<link href="https://fonts.googleapis.com/css2?family=Fredoka:wght@500;600;700&family=Nunito:wght@400;700;800&display=swap" rel="stylesheet">
<style>
  :root{
    --page:#ffffff;
    --meadow:#7cbf3a;
    --meadow-light:#96d04e;
    --meadow-deep:#5fa22a;
    --meadow-ink:#e0353f;
    --swirl:#f08a1c;
    --swirl-light:#f7a53c;
    --swirl-deep:#d9700e;
    --swirl-ink:#ee6a12;
    --badge:#2f6fc4;
    --white:#ffffff;
    --panel:#ffffff;
    --ink:#1f2a1a;
  }
  *{box-sizing:border-box;margin:0;padding:0}
  html,body{width:738px;height:1200px;overflow:hidden;background:var(--page)}
  body{font-family:"Nunito",sans-serif;position:relative}
  .label-set{position:absolute;left:19px;top:470px;width:700px;display:flex;flex-direction:column;gap:46px}
  .label{position:relative;width:700px;height:104px;overflow:hidden}
  .label--meadow{background:var(--meadow);--light:var(--meadow-light);--deep:var(--meadow-deep);--flavour:var(--meadow-ink)}
  .label--swirl{background:var(--swirl);--light:var(--swirl-light);--deep:var(--swirl-deep);--flavour:var(--swirl-ink)}
  .label__waves{position:absolute;inset:0;width:100%;height:100%}
  .label__waves .wave-light{fill:var(--light)}
  .label__waves .wave-deep{fill:var(--deep)}
  .info-panel{position:absolute;left:30px;top:14px;width:68px;height:76px;background:var(--panel)}
  .info-copy{position:absolute;left:110px;top:14px;width:130px;color:var(--white);font-size:5.2px;line-height:1.45}
  .info-copy p{margin-bottom:4px}
  .info-copy .icons{display:flex;gap:5px;margin-top:4px}
  .info-copy .icons svg{width:12px;height:12px}
  .front{position:absolute;left:250px;top:0;width:200px;height:104px}
  .volume{position:absolute;left:8px;top:14px;background:var(--badge);color:var(--white);font:700 7px "Fredoka",sans-serif;padding:2px 6px;border-radius:8px}
  .claim-badge{position:absolute;left:0;top:42px;width:40px;height:40px;border-radius:50%;background:var(--badge);color:var(--white);font:700 6px/1.15 "Fredoka",sans-serif;display:flex;align-items:center;justify-content:center;text-align:center;padding:4px}
  .brand{position:absolute;left:0;right:0;top:8px;text-align:center;font:700 30px/1 "Fredoka",sans-serif;color:var(--white);letter-spacing:.5px}
  .flavour{position:absolute;left:42px;right:14px;top:46px;background:var(--white);border-radius:14px;text-align:center;font:700 15px/24px "Fredoka",sans-serif;color:var(--flavour)}
  .descriptor{position:absolute;left:42px;right:14px;top:76px;text-align:center;font:800 8px "Nunito",sans-serif;color:var(--white);letter-spacing:1.2px}
  .nutrition{position:absolute;left:505px;top:14px;width:165px;color:var(--white);font-size:5.4px}
  .nutrition h3{font:800 6.5px "Nunito",sans-serif;margin-bottom:2px}
  .nutrition .sub{margin-bottom:3px}
  .nutrition table{width:100%;border-collapse:collapse}
  .nutrition td{border-top:.5px solid rgba(255,255,255,.7);padding:1.5px 0}
  .nutrition td:last-child{text-align:right}
</style>
</head>
<body>
<main class="label-set">

  <section class="label label--meadow" aria-label="Crisp Meadow label">
    <svg class="label__waves" viewBox="0 0 700 104" preserveAspectRatio="none" aria-hidden="true">
      <path class="wave-light" d="M0 70 C120 40 220 95 350 62 C480 30 580 90 700 58 L700 104 L0 104Z"/>
      <path class="wave-deep" d="M0 92 C140 78 240 104 360 88 C500 70 600 100 700 86 L700 104 L0 104Z"/>
    </svg>
    <div class="info-panel"></div>
    <div class="info-copy">
      <p>Ingredients: water, sugar, acidity regulator, flavouring, colourant, vitamins, zinc.</p>
      <p>Best before: see cap</p>
      <p>Keep chilled once opened</p>
      <div class="icons">
        <svg viewBox="0 0 12 12"><circle cx="6" cy="6" r="5" fill="none" stroke="#fff" stroke-width="1"/><path d="M3.5 6.5 5.2 8 8.5 4.2" fill="none" stroke="#fff" stroke-width="1"/></svg>
        <svg viewBox="0 0 12 12"><path d="M6 1.5 10 9H2Z" fill="none" stroke="#fff" stroke-width="1"/></svg>
      </div>
    </div>
    <div class="front">
      <span class="volume">300 ml</span>
      <div class="claim-badge">VITAMIN C, B &amp; ZINC</div>
      <div class="brand">Zindelu</div>
      <div class="flavour">Crisp Meadow</div>
      <div class="descriptor">FLAVOURED DRINK</div>
    </div>
    <div class="nutrition">
      <h3>Nutritional Information</h3>
      <div class="sub">Typical values per 100 ml</div>
      <table>
        <tr><td>Energy</td><td>84 kJ</td></tr>
        <tr><td>Protein</td><td>0 g</td></tr>
        <tr><td>Carbohydrate</td><td>5 g</td></tr>
        <tr><td>Sugar</td><td>4.8 g</td></tr>
        <tr><td>Vitamin C</td><td>12 mg</td></tr>
        <tr><td>Zinc</td><td>1.1 mg</td></tr>
      </table>
    </div>
  </section>

  <section class="label label--swirl" aria-label="Golden Swirl label">
    <svg class="label__waves" viewBox="0 0 700 104" preserveAspectRatio="none" aria-hidden="true">
      <path class="wave-light" d="M0 70 C120 40 220 95 350 62 C480 30 580 90 700 58 L700 104 L0 104Z"/>
      <path class="wave-deep" d="M0 92 C140 78 240 104 360 88 C500 70 600 100 700 86 L700 104 L0 104Z"/>
    </svg>
    <div class="info-panel"></div>
    <div class="info-copy">
      <p>Ingredients: water, sugar, acidity regulator, flavouring, colourant, vitamins, zinc.</p>
      <p>Best before: see cap</p>
      <p>Keep chilled once opened</p>
      <div class="icons">
        <svg viewBox="0 0 12 12"><circle cx="6" cy="6" r="5" fill="none" stroke="#fff" stroke-width="1"/><path d="M3.5 6.5 5.2 8 8.5 4.2" fill="none" stroke="#fff" stroke-width="1"/></svg>
        <svg viewBox="0 0 12 12"><path d="M6 1.5 10 9H2Z" fill="none" stroke="#fff" stroke-width="1"/></svg>
      </div>
    </div>
    <div class="front">
      <span class="volume">300 ml</span>
      <div class="claim-badge">VITAMIN C, B &amp; ZINC</div>
      <div class="brand">Zindelu</div>
      <div class="flavour">Golden Swirl</div>
      <div class="descriptor">FLAVOURED DRINK</div>
    </div>
    <div class="nutrition">
      <h3>Nutritional Information</h3>
      <div class="sub">Typical values per 100 ml</div>
      <table>
        <tr><td>Energy</td><td>84 kJ</td></tr>
        <tr><td>Protein</td><td>0 g</td></tr>
        <tr><td>Carbohydrate</td><td>5 g</td></tr>
        <tr><td>Sugar</td><td>4.8 g</td></tr>
        <tr><td>Vitamin C</td><td>12 mg</td></tr>
        <tr><td>Zinc</td><td>1.1 mg</td></tr>
      </table>
    </div>
  </section>

</main>
</body>
</html>
```